Buddhist Center Advertisement

I need a full page single sided 8.5" by 11" flyer for posting around town that describes our upcoming schedule as well as general information about our center. The flyer should be full color and print at 300 DPI. I'm open to a variety of Buddhist imagery, but it should be related to Tibetan Buddhism.
The flyers will be read off bulletin boards so the text shouldn't be too small.
I prefer not to put text over semi-transparent graphics, I think it makes the text too difficult to read.
Target Market(s)
Spiritually minded people seeking instruction in meditation and looking for a new way of relating to themselves and the world, people looking for answers to life's most important questions. The main function of the flyer is to attract new members.
Industry/Entity Type
Town
Requirements
Must have
- 1. our schedule, with class description
Name of Module: "Walking the Path: Meeting Each Day with a Calm Heart"
In this module we will consider well the disadvantages of self-cherishing and the advantages of cherishing others more than ourselves. We will learn how to employ the special techniques of mind training or “lo-jong” as a means to transform problems into happiness, and learn to treat our challenges as precious opportunities for spiritual growth.
Saturday, September 21 10:30 - 12:30
Saturday, September 28 10:30 - 12:30
Saturday, October 26 10:30 - 12:30
Saturday, November 9 10:30 - 6:00 Retreat Day
Saturday, November 23 10:30 - 6:00 Retreat Day
2. Our website, www.velorinda-sangha.example
3. our phone number (555) 318-2046
4. Our facebook and Meetup pages
https://www.social-example.com/VelorindaCenter
http://www.groups-example.com/velorinda-buddhist-center/
5. This text
"The Velorinda center is a community of spiritual friends dedicated to the practice of Tibetan Buddhism. We practice in the Gelugpa tradition, the same lineage as his Holiness The Ombar Tsendo. The Center was founded in 1994 under the spiritual direction of Geshe Tenkor Dawa, and the Society for the Continuance of the Vajrodha Heritage. We offer weekly classes in meditation and Buddhist philosophy suitable for beginners as well as advanced practitioners. All classes are free of charge and offered on a donation basis only.
Nice to have
- our logo

```html
<!DOCTYPE html>
<html lang="en">
<head>
<meta charset="utf-8">
<title>Walking the Path – Velorinda Center Flyer</title>
<link rel="stylesheet" href="https://fonts.googleapis.com/css2?family=Ubuntu:wght@500;700&family=Arimo:wght@400;700&family=Crimson+Text:ital@0;1&display=swap">
<style>
  :root {
    --page-bg: #2a2a2a;
    --night-dark: #1c1d20;
    --night-mid: #4a4a4e;
    --night-light: #8a8680;
    --orange: #f08a2c;
    --orange-deep: #e2701a;
    --orange-light: #f7a451;
    --paper: #eeeceb;
    --paper-shade: #d6d3cf;
    --ribbon-red: #d3262a;
    --ribbon-dark: #8f1416;
    --card: #f4f4f4;
    --ink-grey: #5f5f5f;
    --ink-dark: #333333;
    --white: #ffffff;
    --icon-blue: #2f78c4;
  }
  * { box-sizing: border-box; margin: 0; padding: 0; }
  html, body { width: 1200px; height: 1000px; overflow: hidden; }
  body { background: var(--page-bg); position: relative; font-family: "Arimo", Arial, sans-serif; }

  .flyer {
    position: absolute; left: 229px; top: 20px;
    width: 742px; height: 960px; overflow: hidden;
    background: var(--paper);
  }

  /* Header with skyline photo */
  .header-photo {
    position: absolute; left: 0; top: 0; width: 742px; height: 278px;
    background: linear-gradient(180deg, var(--night-dark) 0%, var(--night-mid) 55%, var(--night-light) 100%);
  }
  .brand {
    position: absolute; left: 22px; top: 22px; width: 190px; text-align: center; color: var(--white);
  }
  .brand-mark {
    width: 130px; height: 130px; border-radius: 50%; margin: 0 auto 10px;
    border: 2px solid rgba(255,255,255,0.8);
    display: flex; align-items: center; justify-content: center;
  }
  .brand-name { font-family: "Ubuntu", sans-serif; font-weight: 500; font-size: 19px; color: var(--white); }
  .brand-quote { font-family: "Crimson Text", serif; font-size: 16px; line-height: 1.2; }
  .brand-quote cite { display: block; font-style: normal; font-size: 13px; }

  .module-title {
    position: absolute; left: 262px; top: 110px; color: var(--white);
    font-family: "Ubuntu", sans-serif; font-weight: 700; letter-spacing: 0.5px;
    text-shadow: 2px 2px 3px rgba(0,0,0,0.6);
  }
  .module-title .kicker { display: block; font-size: 28px; margin-bottom: 8px; }
  .module-title .main { display: block; font-size: 35px; line-height: 1.3; }

  /* Description band */
  .intro-band {
    position: absolute; left: 0; top: 278px; width: 742px; height: 158px;
    background: linear-gradient(100deg, var(--orange-light), var(--orange) 45%, var(--orange-deep));
    padding: 18px 30px;
    color: var(--white); font-size: 16px; line-height: 1.5; font-weight: 700;
    text-shadow: 0 1px 1px rgba(0,0,0,0.15);
  }

  /* Schedule area over desk photo */
  .desk-photo {
    position: absolute; left: 0; top: 436px; width: 742px; height: 306px;
    background: linear-gradient(135deg, var(--paper) 0%, #ffffff 40%, var(--paper-shade) 100%);
  }
  .schedule { position: absolute; left: 36px; top: 464px; display: flex; gap: 16px; }
  .schedule-card {
    width: 190px; height: 258px; background: var(--card);
    border-radius: 0 0 8px 8px; position: relative;
    box-shadow: 3px 4px 8px rgba(0,0,0,0.3);
  }
  .schedule-card header {
    position: absolute; left: -8px; top: -8px; width: 206px; height: 40px;
    background: linear-gradient(180deg, #e4393c, var(--ribbon-red));
    color: var(--white); font-weight: 700; font-size: 21px;
    display: flex; align-items: center; justify-content: center;
    box-shadow: 0 3px 4px rgba(0,0,0,0.3);
  }
  .schedule-card header::before, .schedule-card header::after {
    content: ""; position: absolute; bottom: -8px; border-top: 8px solid var(--ribbon-dark);
  }
  .schedule-card header::before { left: 0; border-left: 8px solid transparent; }
  .schedule-card header::after { right: 0; border-right: 8px solid transparent; }
  .schedule-card ul { list-style: none; padding: 46px 0 0 14px; }
  .schedule-card li {
    height: 42px; font-size: 19px; font-weight: 700; color: var(--ink-grey); line-height: 1.1;
  }
  .schedule-card li small { display: block; font-size: 12px; font-weight: 400; padding-left: 44px; }

  .contact-box {
    position: absolute; left: 432px; top: 556px; width: 290px; height: 180px;
    background: var(--white); border: 1px solid #cfcfcf;
    box-shadow: 2px 3px 6px rgba(0,0,0,0.25);
    padding: 10px 10px; color: var(--ink-dark); font-style: normal;
  }
  .contact-row { display: flex; align-items: center; gap: 14px; font-size: 15px; height: 34px; }
  .contact-row .icon { width: 22px; height: 22px; flex: none; }
  .contact-row.phone span { padding-left: 50px; }
  .contact-link { font-size: 10.5px; margin: 0 0 6px 0; white-space: nowrap; }
  .social-dot { display: block; width: 22px; height: 22px; border-radius: 50%; background: var(--icon-blue); margin-bottom: 3px; }
  .social-square { display: block; width: 22px; height: 16px; background: var(--ribbon-red); margin-bottom: 3px; }

  /* Footer band */
  .about-band {
    position: absolute; left: 0; top: 742px; width: 742px; height: 218px;
    background: linear-gradient(100deg, var(--orange-deep), var(--orange) 50%, var(--orange-light));
    padding: 20px 30px; color: var(--white); font-size: 15px; line-height: 1.55; font-weight: 700;
  }
  .about-band .note { margin-top: 8px; text-align: center; }
</style>
</head>
<body>
<main class="flyer">
  <div class="header-photo" role="img" aria-label="Night city skyline photograph in dark grey tones"></div>

  <div class="brand">
    <div class="brand-mark"><span class="brand-name">Velorinda</span></div>
    <p class="brand-quote">"For Happiness, Cherish Others."<cite>Geshe Tenkor Dawa</cite></p>
  </div>

  <h1 class="module-title">
    <span class="kicker">Walking the Path:</span>
    <span class="main">Meeting Each Day<br>with a Calm Heart..</span>
  </h1>

  <section class="intro-band">
    In this module we will consider well the disadvantages of self-cherishing and the advantages of cherishing others more than ourselves. We will learn how to employ the special techniques of mind training or “lo-jong” as a means to transform problems into happiness and learn to treat our challenges as precious opportunities for spiritual growth.
  </section>

  <div class="desk-photo" role="img" aria-label="Photograph of papers with printed charts and a pen on a desk, in pale grey tones"></div>

  <section class="schedule">
    <div class="schedule-card">
      <header>Date</header>
      <ul>
        <li>-Saturday, 21Sep</li>
        <li>-Saturday, 28Sep</li>
        <li>-Saturday, 26Oct</li>
        <li>-Saturday, 09Nov</li>
        <li>-Saturday, 23Nov</li>
      </ul>
    </div>
    <div class="schedule-card">
      <header>Time</header>
      <ul>
        <li>10:30 - 12:30</li>
        <li>10:30 - 12:30</li>
        <li>10:30 - 12:30</li>
        <li>10:30 - 6:00<small>Retreat Day</small></li>
        <li>10:30 - 6:00<small>Retreat Day</small></li>
      </ul>
    </div>
  </section>

  <address class="contact-box">
    <div class="contact-row">
      <svg class="icon" viewBox="0 0 22 22"><rect width="22" height="22" fill="var(--icon-blue)"/><rect x="4" y="3" width="16" height="16" fill="#fff"/><text x="12" y="16" font-size="13" text-anchor="middle" fill="var(--icon-blue)" font-family="Arimo, sans-serif">@</text></svg>
      <span>www.velorinda-sangha.example</span>
    </div>
    <div class="contact-row phone">
      <svg class="icon" viewBox="0 0 22 22"><path d="M3 9c0-4 16-4 16 0l-3 2-2-2H8L6 11z M6 12h10l3 7H3z" fill="#8aa9c4"/></svg>
      <span>(555) 318-2046</span>
    </div>
    <span class="social-dot"></span>
    <p class="contact-link">www.social-example.com/VelorindaCenter</p>
    <span class="social-square"></span>
    <p class="contact-link">www.groups-example.com/velorinda-buddhist-center</p>
  </address>

  <section class="about-band">
    <p>The Velorinda center is a community of spiritual friends dedicated to the practice of Tibetan Buddhism. We practice in the Gelugpa tradition, the same lineage as his Holiness The Ombar Tsendo. The Center was founded in 1994 under the spiritual direction of Geshe Tenkor Dawa, and the Society for the Continuance of the Vajrodha Heritage. We offer weekly classes in meditation and Buddhist philosophy suitable for beginners as well as advanced practitioners.</p>
    <p class="note">All classes are free of charge and offered on a donation basis only.</p>
  </section>
</main>
</body>
</html>
```